Web Design Project

i'm looking for a sleek modern design i can use for a web site that deals with.
Intelligent Data Capture
Accounts Payable Solutions for faster processing based on our scanning solution.
ultimately we are a intelligent scanning software.

here is a great website, that does exactly what we do, and we like to have most of their services and products.

so something in this idea would be great.
www.dravolin.com

so i guess i want a good landing/home page which is smartly designed so users will be inclined to leave their information.

and then information pages.

also i dont need any cms for you to include, i only need you to hook the html hooks for RANK Kettle as i already have a CMS and need it to hook in to that, i am including links to that cheat sheet.
so it is easier when included as you create the Theme.

http://www.rankkettle.com/how-to-create-website-template.html
http://www.rankkettle.com/cheat-sheet.html
Updates

Hi Guys sorry for the long pause in design, but here is where we stand.

what ever design i choose, i need that designer to customize a few things for me based on design that was designed.
and i will need designer to match that them to work with RANK Kettle
here is the cheat sheet for the hooks that we need to match and make it work.
if you have any questions let me know.

otherwise i look forward to working with you. and good luck.

Target Market(s)

CFO's AP Managers, mostly ppl who are not Tech freindly

Industry/Entity Type

Software

Requirements
Must have
• i need on home page, the rotating banner should have 1 ability to place vidmora links to show videos, and also ability to add buttons on these rotating banners that will allow forms to pop up take to another page.

```html
<!DOCTYPE html>
<html lang="en">
<head>
<meta charset="utf-8">
<title>Intelligent Data Capture – Home</title>
<link rel="stylesheet" href="https://fonts.googleapis.com/css2?family=Carlito:wght@400;700&family=Cinzel:wght@400;600&family=Tinos&display=swap">
<style>
  :root {
    --topline: #0b0d0e;
    --header: #37444e;
    --hero: #bdd0d9;
    --tab: #c2d3dc;
    --heading: #3f4449;
    --body-grey: #555b60;
    --sub-grey: #737c82;
    --accent-blue: #1a5ea8;
    --green: #8cc02c;
    --services-bg: #bfd0d9;
    --services-text: #6b7277;
    --bottom: #1d262b;
    --white: #ffffff;
    --rule: #d5d9dc;
  }
  * { box-sizing: border-box; margin: 0; padding: 0; }
  html, body { width: 1200px; height: 1200px; overflow: hidden; background: var(--white); }
  body { position: relative; font-family: "Carlito", "Calibri", sans-serif; }
  .abs { position: absolute; }

  .top-line { left: 0; top: 0; width: 1200px; height: 14px; background: var(--topline); }
  .site-header { left: 0; top: 14px; width: 1200px; height: 136px; background: var(--header); }
  .call-badge { left: 978px; top: 12px; width: 108px; height: 17px; background: #111; color: var(--white);
    font-family: "Tinos", serif; font-size: 10px; line-height: 17px; text-align: center; border-radius: 0 0 3px 3px; }
  .brand { left: 96px; top: 84px; color: var(--white); font-weight: 700; font-size: 40px; letter-spacing: 0.5px; }

  .main-nav a { position: absolute; top: 110px; font-family: "Cinzel", serif; font-size: 20px; color: var(--white); text-decoration: none; }
  .nav-tab { left: 458px; top: 102px; width: 95px; height: 48px; background: var(--tab); border-radius: 3px 3px 0 0; }
  .main-nav a.is-active { left: 458px; width: 95px; text-align: center; color: #1e2a32; }

  .hero { left: 0; top: 150px; width: 1200px; height: 310px; background: var(--hero); }
  .hero-title { left: 98px; top: 185px; font-size: 40px; font-weight: 700; color: var(--heading); }
  .hero-text { left: 104px; top: 236px; width: 405px; font-size: 15.5px; line-height: 19.9px; font-weight: 700; color: var(--white); }
  .btn-demo { left: 100px; top: 395px; width: 124px; height: 26px; border-radius: 13px; background: var(--white);
    border: 2px solid #4a5056; box-shadow: 1px 2px 2px rgba(0,0,0,.35); font-size: 14px; font-weight: 700; color: #30363b;
    line-height: 22px; text-align: center; white-space: nowrap; text-decoration: none; }
  .slider-frame { left: 594px; top: 184px; width: 462px; height: 243px; background: var(--white); border-radius: 4px;
    box-shadow: 2px 3px 6px rgba(0,0,0,.35); padding: 5px; }
  .slider-photo { width: 100%; height: 100%; background: linear-gradient(180deg, #1f5fa8 0%, #4f93d3 55%, #bcd8ee 80%, #2f5e90 100%); }
  .video-play { left: 799px; top: 280px; width: 52px; height: 52px; }
  .slider-arrow { top: 277px; width: 28px; height: 47px; }
  .slider-arrow.prev { left: 568px; }
  .slider-arrow.next { left: 1056px; }

  .welcome-title { left: 104px; top: 502px; font-size: 27px; font-weight: 700; letter-spacing: 3px; color: var(--heading); }
  .welcome-title span { color: var(--accent-blue); }
  .welcome-text { left: 104px; top: 541px; width: 585px; font-size: 19px; line-height: 24.5px; font-weight: 700; letter-spacing: 1.6px; color: var(--body-grey); }
  .rule { left: 101px; width: 648px; height: 2px; background: var(--rule); }
  .firm-line { left: 101px; top: 680px; font-size: 18.5px; font-weight: 700; letter-spacing: 1.5px; color: var(--sub-grey); }

  .feature-thumb { top: 728px; width: 213px; height: 116px; border: 2px solid #585f64; box-shadow: 1px 2px 4px rgba(0,0,0,.35); }
  .thumb-a { left: 98px; background: linear-gradient(135deg, #dbe6ef, #8fb0c8 60%, #c9d9e4); }
  .thumb-b { left: 326px; background: linear-gradient(135deg, #f3f6f9, #7f9fc4 55%, #e8eef4); }
  .thumb-c { left: 552px; background: linear-gradient(180deg, #1b62c6, #5aa6ea 60%, #d8ecfa); }
  .feature-caption { top: 857px; width: 210px; font-size: 12px; line-height: 15px; font-weight: 700; color: #444a4f; }

  .services { left: 799px; top: 499px; width: 302px; height: 401px; background: var(--services-bg); border: 1px solid #8a98a1;
    box-shadow: 1px 2px 4px rgba(0,0,0,.3); }
  .services-head { height: 69px; background: linear-gradient(180deg, #eaf5fb, #c6dfec); color: var(--heading);
    font-size: 29px; font-weight: 700; text-align: center; line-height: 66px; }
  .services-list { list-style: none; position: absolute; left: 0; top: 0; width: 100%; }
  .services-list li { position: absolute; left: 20px; height: 30px; font-size: 26.5px; font-weight: 700; color: var(--services-text);
    line-height: 30px; padding-left: 34px; white-space: nowrap; }
  .services-list svg { position: absolute; left: 0; top: 8px; }

  .footer-band { left: 0; top: 948px; width: 1200px; height: 202px; background: var(--header); }
  .footer-tab { top: 930px; width: 275px; height: 85px; background: var(--green); color: var(--white); font-size: 26.5px;
    font-weight: 700; text-align: center; line-height: 82px; }
  .tab-fold { top: 930px; width: 12px; height: 18px; }
  .footer-text { top: 1032px; width: 210px; font-size: 12px; line-height: 15px; font-weight: 700; color: var(--white); }

  .footer-nav { top: 1121px; font-family: "Cinzel", serif; font-size: 20px; color: var(--white); }
  .footer-home { left: 251px; top: 1122px; width: 85px; height: 24px; border-radius: 12px; background: #c8d2d8; color: #5c6a73;
    text-align: center; line-height: 24px; font-family: "Cinzel", serif; font-size: 20px; }
  .bottom-bar { left: 0; top: 1150px; width: 1200px; height: 50px; background: var(--bottom); }
  .copyright { left: 523px; top: 1161px; font-family: "Tinos", serif; font-size: 21px; color: #c9ced1; }
</style>
</head>
<body>
  <div class="abs top-line"></div>
  <header class="abs site-header"></header>
  <div class="abs call-badge"><b>CALL</b> - 555-010-0199</div>
  <div class="abs brand">COMPANY LOGO</div>

  <nav class="main-nav">
    <div class="abs nav-tab"></div>
    <a class="is-active" href="#">Home</a>
    <a href="#" style="left:572px">Solutions</a>
    <a href="#" style="left:716px">Services</a>
    <a href="#" style="left:844px">About Us</a>
    <a href="#" style="left:978px">Contact Us</a>
  </nav>

  <section class="abs hero"></section>
  <h1 class="abs hero-title">BUSINESS SOLUTION</h1>
  <p class="abs hero-text">Intelligent data capture that turns scanned invoices into clean, ready-to-post data. Our Accounts Payable solution reads every field, matches it to your purchase orders and routes it for approval, so your team clears more invoices in less time. No technical skills needed. Watch the short video or leave your details and we will call you.</p>
  <a class="abs btn-demo" href="#request-demo">Request A Demo</a>

  <div class="abs slider-frame"><div class="slider-photo" role="img" aria-label="Banner video still: business people silhouetted against a blue world map"></div></div>
  <svg class="abs video-play" viewBox="0 0 52 52" role="img" aria-label="Play video">
    <circle cx="26" cy="26" r="24" fill="rgba(0,0,0,.45)" stroke="#fff" stroke-width="2"/>
    <path d="M21 16 L37 26 L21 36 Z" fill="#fff"/>
  </svg>
  <svg class="abs slider-arrow prev" viewBox="0 0 28 47" aria-hidden="true">
    <rect width="28" height="47" fill="#6cbf3a" stroke="#3f8a1e"/>
    <path d="M20 13 L8 23.5 L20 34 Z" fill="#fff"/>
  </svg>
  <svg class="abs slider-arrow next" viewBox="0 0 28 47" aria-hidden="true">
    <rect width="28" height="47" fill="#6cbf3a" stroke="#3f8a1e"/>
    <path d="M8 13 L20 23.5 L8 34 Z" fill="#fff"/>
  </svg>

  <h2 class="abs welcome-title">WELCOME TO <span>OUR WEBSITE</span></h2>
  <p class="abs welcome-text">Our intelligent scanning software captures data from invoices and forms, checks it against your records and sends it straight to your accounts system, so AP teams stop typing..</p>
  <div class="abs rule" style="top:666px"></div>
  <h3 class="abs firm-line">Faster Invoice Processing For Finance Teams</h3>
  <div class="abs rule" style="top:711px"></div>

  <div class="abs feature-thumb thumb-a" role="img" aria-label="Illustration: two hands reaching toward each other over a digital backdrop"></div>
  <div class="abs feature-thumb thumb-b" role="img" aria-label="Illustration: a hand pressing among floating app icons"></div>
  <div class="abs feature-thumb thumb-c" role="img" aria-label="Photo: a hand touching a glass panel against a blue sky"></div>
  <p class="abs feature-caption" style="left:101px">Scan any paper or PDF invoice and the key fields are read for you automatically.</p>
  <p class="abs feature-caption" style="left:326px">Invoices are matched to purchase orders and sent on for approval in one click.</p>
  <p class="abs feature-caption" style="left:551px">Approved data posts straight into your accounts system, with no retyping at all.</p>

  <aside class="abs services">
    <div class="services-head">OUR SERVICES</div>
    <ul class="services-list">
      <li style="top:81px"><svg width="20" height="14" viewBox="0 0 20 14"><path d="M2 1 L18 7 L2 13 L7 7 Z" fill="#fff"/></svg>Data Capture</li>
      <li style="top:127px"><svg width="20" height="14" viewBox="0 0 20 14"><path d="M2 1 L18 7 L2 13 L7 7 Z" fill="#fff"/></svg>Invoice Scanning</li>
      <li style="top:173px"><svg width="20" height="14" viewBox="0 0 20 14"><path d="M2 1 L18 7 L2 13 L7 7 Z" fill="#fff"/></svg>AP Automation</li>
      <li style="top:218px"><svg width="20" height="14" viewBox="0 0 20 14"><path d="M2 1 L18 7 L2 13 L7 7 Z" fill="#fff"/></svg>Customer Care</li>
      <li style="top:264px"><svg width="20" height="14" viewBox="0 0 20 14"><path d="M2 1 L18 7 L2 13 L7 7 Z" fill="#fff"/></svg>Free Quote</li>
      <li style="top:309px"><svg width="20" height="14" viewBox="0 0 20 14"><path d="M2 1 L18 7 L2 13 L7 7 Z" fill="#fff"/></svg>Free Guide</li>
      <li style="top:355px"><svg width="20" height="14" viewBox="0 0 20 14"><path d="M2 1 L18 7 L2 13 L7 7 Z" fill="#fff"/></svg>Online Demo</li>
    </ul>
  </aside>

  <footer class="abs footer-band"></footer>
  <svg class="abs tab-fold" style="left:98px" viewBox="0 0 12 18" aria-hidden="true"><path d="M12 0 L12 18 L0 18 Z" fill="#4b5a25"/></svg>
  <svg class="abs tab-fold" style="left:385px" viewBox="0 0 12 18" aria-hidden="true"><path d="M0 0 L0 18 L12 18 Z" fill="#4b5a25"/></svg>
  <svg class="abs tab-fold" style="left:451px" viewBox="0 0 12 18" aria-hidden="true"><path d="M12 0 L12 18 L0 18 Z" fill="#4b5a25"/></svg>
  <svg class="abs tab-fold" style="left:738px" viewBox="0 0 12 18" aria-hidden="true"><path d="M0 0 L0 18 L12 18 Z" fill="#4b5a25"/></svg>
  <svg class="abs tab-fold" style="left:802px" viewBox="0 0 12 18" aria-hidden="true"><path d="M12 0 L12 18 L0 18 Z" fill="#4b5a25"/></svg>
  <svg class="abs tab-fold" style="left:1088px" viewBox="0 0 12 18" aria-hidden="true"><path d="M0 0 L0 18 L12 18 Z" fill="#4b5a25"/></svg>
  <div class="abs footer-tab" style="left:110px">News And Updates</div>
  <div class="abs footer-tab" style="left:463px">Latest Blog Post</div>
  <div class="abs footer-tab" style="left:814px">Recent Comments</div>
  <p class="abs footer-text" style="left:115px">New release: invoice capture now reads line items and tax fields on every scan.</p>
  <p class="abs footer-text" style="left:466px">Five ways finance teams cut invoice processing time with smart scanning.</p>
  <p class="abs footer-text" style="left:815px">"Our AP team now clears a week of invoices in a single afternoon."</p>

  <div class="abs footer-home">Home</div>
  <div class="abs footer-nav" style="left:342px">|</div>
  <div class="abs footer-nav" style="left:369px">Solutions</div>
  <div class="abs footer-nav" style="left:502px">|</div>
  <div class="abs footer-nav" style="left:523px">Services</div>
  <div class="abs footer-nav" style="left:640px">|</div>
  <div class="abs footer-nav" style="left:660px">About Us</div>
  <div class="abs footer-nav" style="left:777px">|</div>
  <div class="abs footer-nav" style="left:803px">Contact Us</div>

  <div class="abs bottom-bar"></div>
  <div class="abs copyright">Copyright © Norvale 2012</div>
</body>
</html>
```